Ferro Lanes - explore habits of productive people

Ferro Lanes is a social place around habits and productivity

The full brief below:

https://files.quorvanta.com/sheet/d/7Kp-RwTZMX2uqEebH-Y-cNdt4TgsWmFkyQoPJhwbrzVe/view?mode=viewer

Colors

Designer to choose colors to be used in the design.

Requirements
Must have
• - a feed page to display habits
• - a habit page to add a habit
• / clean, no cluttered design, lots of white space
• / inspired by material design or other design system
Nice to have
• - user page

```html
<!DOCTYPE html>
<html lang="en">
<head>
<meta charset="utf-8">
<title>Ferro Lanes – My feed</title>
<link href="https://fonts.googleapis.com/css2?family=Montserrat:wght@400;500;600&display=swap" rel="stylesheet">
<style>
  :root {
    --brand-blue: #2b7ff2;
    --link-blue: #2a7de8;
    --page-bg: #f2f2f2;
    --card-bg: #ffffff;
    --ink: #1d1d1d;
    --muted: #c4c4c4;
    --good: #1ccf68;
    --good-dim: #bdf1d3;
    --bad: #e3321f;
    --bad-dim: #f5c5c0;
    --avatar: #6b4a3c;
    --shadow: 0 1px 4px rgba(0,0,0,0.06);
  }
  * { box-sizing: border-box; margin: 0; padding: 0; }
  html, body { width: 1200px; height: 676px; overflow: hidden; }
  body {
    position: relative;
    background: var(--page-bg);
    font-family: "Montserrat", sans-serif;
    color: var(--ink);
  }
  .topbar {
    position: absolute; left: 0; top: 0; width: 1200px; height: 55px;
    background: var(--brand-blue);
  }
  .brand {
    position: absolute; left: 199px; top: 17px;
    font-size: 19px; font-weight: 500; color: #fff; line-height: 22px;
  }
  .new-habit {
    position: absolute; left: 763px; top: 18px;
    display: flex; align-items: center; gap: 8px;
    color: #fff; font-size: 11px; font-weight: 500;
  }
  .user {
    position: absolute; left: 876px; top: 11px;
    display: flex; align-items: center; gap: 12px;
    color: #fff; font-size: 11px; font-weight: 500;
  }
  .user-avatar {
    position: relative; width: 34px; height: 34px; border-radius: 50%;
    background: radial-gradient(circle at 50% 40%, #b98a72, var(--avatar));
  }
  .badge {
    position: absolute; left: 2px; bottom: -4px; width: 11px; height: 11px;
    border-radius: 50%; background: #fff; color: var(--brand-blue);
    font-size: 7px; font-weight: 600; text-align: center; line-height: 11px;
  }
  .page-title {
    position: absolute; left: 200px; top: 81px;
    font-size: 16px; font-weight: 500; line-height: 20px;
  }
  .habit-card {
    position: absolute; left: 200px; width: 498px; height: 309px;
    background: var(--card-bg); border-radius: 4px; box-shadow: var(--shadow);
    padding: 19px 20px 0 18px; overflow: hidden;
  }
  .habit-card.second { top: 450px; height: 240px; }
  .habit-card.first { top: 115px; }
  .habit-head {
    display: flex; justify-content: space-between; align-items: center; height: 16px;
  }
  .habit-name { color: var(--link-blue); font-size: 13.5px; font-weight: 500; }
  .verdict { display: flex; gap: 10px; font-size: 12px; font-weight: 500; }
  .good { color: var(--good); }
  .good.off { color: var(--good-dim); }
  .bad { color: var(--bad); }
  .bad.off { color: var(--bad-dim); }
  .step { margin-top: 14px; padding-left: 2px; }
  .step:first-of-type { margin-top: 11px; }
  .step h3 { font-size: 13px; font-weight: 500; line-height: 15px; }
  .step p { font-size: 10.5px; line-height: 12px; width: 470px; }
  .adopt-count { margin-top: 16px; font-size: 9px; font-weight: 500; color: var(--muted); line-height: 11px; }
  .adopt {
    margin-top: 7px; display: flex; align-items: center; gap: 5px;
    color: var(--bad); font-size: 10px; font-weight: 600; line-height: 12px;
  }
  .activity {
    position: absolute; left: 728px; top: 115px; width: 273px; height: 447px;
    background: var(--card-bg); border-radius: 4px; box-shadow: var(--shadow);
    padding: 13px 18px 0 18px;
  }
  .activity h2 { font-size: 15.5px; font-weight: 500; line-height: 18px; }
  .activity ul { list-style: none; margin-top: 9px; }
  .activity li {
    display: flex; gap: 6px; height: 45px; padding-left: 4px;
  }
  .mini-avatar {
    flex: none; width: 24px; height: 24px; border-radius: 50%; margin-top: 2px;
    background: radial-gradient(circle at 50% 40%, #b98a72, var(--avatar));
  }
  .activity p { font-size: 10.5px; line-height: 12px; }
  .activity a { color: var(--link-blue); text-decoration: none; }
</style>
</head>
<body>
  <header class="topbar">
    <div class="brand">Ferro Lanes</div>
    <div class="new-habit">
      <svg width="19" height="19" viewBox="0 0 20 20" aria-hidden="true">
        <circle cx="10" cy="10" r="9" fill="none" stroke="#fff" stroke-width="1.4"/>
        <path d="M10 5.5v9M5.5 10h9" stroke="#fff" stroke-width="1.4"/>
      </svg>
      <span>New habit</span>
    </div>
    <div class="user">
      <div class="user-avatar" role="img" aria-label="Profile photo of tessaform">
        <span class="badge">2</span>
      </div>
      <span>tessaform</span>
    </div>
  </header>

  <h1 class="page-title">My feed</h1>

  <article class="habit-card first">
    <div class="habit-head">
      <span class="habit-name">Habit name</span>
      <span class="verdict"><span class="good">Good</span><span class="bad off">Bad</span></span>
    </div>
    <section class="step"><h3>Cue</h3><p>Ut enim ad minim veniam, quis nostrud exercitation ullamco laboris nisi ut aliquip ex ea commodo consequat.</p></section>
    <section class="step"><h3>Craving</h3><p>Sed ut perspiciatis unde omnis iste natus error sit voluptatem accusantium doloremque laudantium, totam rem aperia.</p></section>
    <section class="step"><h3>Response</h3><p>Nemo enim ipsam voluptatem quia voluptas sit aspernatur aut odit aut fugit, sed quia consequuntur magni dolores eos qui ratione.</p></section>
    <section class="step"><h3>Reward</h3><p>Neque porro quisquam est, qui dolorem ipsum quia dolor sit amet, consectetur, adipisci velit, sed quia non numquam eius modi tempora incidunt ut labore.</p></section>
    <div class="adopt-count">27 people have adopted this habit</div>
    <div class="adopt">
      <svg width="12" height="11" viewBox="0 0 24 22" aria-hidden="true">
        <path d="M12 21.5 2.6 12.3C-0.6 9 0.4 3.6 4.6 2.1 7.4 1 10.3 2.2 12 4.6 13.7 2.2 16.6 1 19.4 2.1c4.2 1.5 5.2 6.9 2 10.2z" fill="#e3321f"/>
      </svg>
      <span>Adopt</span>
    </div>
  </article>

  <article class="habit-card second">
    <div class="habit-head">
      <span class="habit-name">Habit name</span>
      <span class="verdict"><span class="good off">Good</span><span class="bad">Bad</span></span>
    </div>
    <section class="step"><h3>Cue</h3><p>Ut enim ad minim veniam, quis nostrud exercitation ullamco laboris nisi ut aliquip ex ea commodo consequat.</p></section>
    <section class="step"><h3>Craving</h3><p>Sed ut perspiciatis unde omnis iste natus error sit voluptatem accusantium doloremque laudantium, totam rem aperia.</p></section>
    <section class="step"><h3>Response</h3><p>Nemo enim ipsam voluptatem quia voluptas sit aspernatur aut odit aut fugit, sed quia consequuntur magni dolores eos qui ratione.</p></section>
    <section class="step"><h3>Reward</h3><p>Neque porro quisquam est, qui dolorem ipsum quia dolor sit amet, consectetur, adipisci velit, sed quia non numquam eius modi tempora incidunt ut labore.</p></section>
  </article>

  <aside class="activity">
    <h2>Recent Activity</h2>
    <ul>
      <li><div class="mini-avatar" role="img" aria-label="Profile photo of Dario Venkel"></div><p>Dario Venkel has adopted the habit <a href="#">habit name</a></p></li>
      <li><div class="mini-avatar" role="img" aria-label="Profile photo of Dario Venkel"></div><p>Dario Venkel has adopted the habit <a href="#">habit name</a></p></li>
      <li><div class="mini-avatar" role="img" aria-label="Profile photo of Dario Venkel"></div><p>Dario Venkel has adopted the habit <a href="#">habit name</a></p></li>
      <li><div class="mini-avatar" role="img" aria-label="Profile photo of Dario Venkel"></div><p>Dario Venkel has adopted the habit <a href="#">habit name</a></p></li>
      <li><div class="mini-avatar" role="img" aria-label="Profile photo of Dario Venkel"></div><p>Dario Venkel has adopted the habit <a href="#">habit name</a></p></li>
      <li><div class="mini-avatar" role="img" aria-label="Profile photo of Dario Venkel"></div><p>Dario Venkel has adopted the habit <a href="#">habit name</a></p></li>
      <li><div class="mini-avatar" role="img" aria-label="Profile photo of Dario Venkel"></div><p>Dario Venkel has adopted the habit <a href="#">habit name</a></p></li>
    </ul>
  </aside>
</body>
</html>
```